Modern Business Card for Speech Therapy Practice
Clear Sound Harbor LLC
Bright & Fun-filled
Odile Varnet, M.A., CCC-SLP
827 Quarry Ln.
Lowmere, KV 07391
Odile.Varnet@mailbrook.net
www.ClearSoundHarbor.net
NJ Lic: 58KT00394817

```html
<!DOCTYPE html>
<html lang="en">
<head>
<meta charset="utf-8">
<title>Clear Sound Harbor LLC – Business Card Set</title>
<link rel="stylesheet" href="https://fonts.googleapis.com/css2?family=Arimo:wght@400;700&family=Cinzel:wght@400&display=swap">
<style>
  :root {
    --board: #3b2a22;
    --card: #fbfbfa;
    --orange: #ef7a22;
    --green: #7cbf3c;
    --navy: #27365f;
    --ink: #3c3c3c;
    --label: #f1ece6;
  }
  * { margin: 0; padding: 0; box-sizing: border-box; }
  html, body { width: 1200px; height: 825px; overflow: hidden; }
  body { background: var(--board); font-family: "Arimo", Arial, sans-serif; position: relative; }

  .card { position: absolute; width: 550px; height: 302px; background: var(--card);
          box-shadow: 0 3px 8px rgba(0,0,0,.45); overflow: hidden; }
  .card--front-1 { left: 34px;  top: 34px; }
  .card--front-2 { left: 617px; top: 34px; }
  .card--back-1  { left: 34px;  top: 420px; }
  .card--back-2  { left: 617px; top: 420px; }

  .edge-band { position: absolute; top: 0; width: 26px; height: 302px; }
  .edge-band--left { left: 0; }
  .edge-band--right { right: 0; }

  .label { position: absolute; width: 550px; text-align: center;
           font-family: "Cinzel", Georgia, serif; font-size: 20px; color: var(--label); }
  .label--front-1 { left: 34px;  top: 350px; }
  .label--front-2 { left: 617px; top: 350px; }
  .label--back-1  { left: 34px;  top: 752px; }
  .label--back-2  { left: 617px; top: 752px; }

  .brand { position: absolute; display: flex; align-items: center; gap: 8px;
           font-family: "Arimo", Arial, sans-serif; font-weight: 700; color: var(--navy); white-space: nowrap; }
  .brand__dot { width: 14px; height: 14px; border-radius: 50%; background: var(--orange); flex: none; }

  .contact { position: absolute; font-size: 11.5px; line-height: 15px; color: var(--ink); }
  .contact__name { color: var(--green); font-size: 13px; margin-bottom: 12px; }
  .contact__row { display: flex; align-items: center; gap: 4px; }
  .bullet { width: 8px; height: 8px; border-radius: 50%; flex: none; }
  .bullet--green { background: var(--green); }
  .bullet--orange { background: var(--orange); }

  .website { position: absolute; left: 0; width: 100%; text-align: center; font-size: 11px; color: var(--ink); }
</style>
</head>
<body>

  <section class="card card--front-1">
    <svg class="edge-band edge-band--left" viewBox="0 0 26 302" aria-hidden="true">
      <polygon points="0,0 26,0 26,130 0,160" fill="var(--orange)"/>
      <polygon points="0,166 26,136 26,302 0,302" fill="var(--green)"/>
    </svg>
    <div class="brand" style="right:40px; top:100px; font-size:18px;">
      <span class="brand__dot"></span>Clear Sound Harbor
    </div>
    <div class="contact" style="left:60px; top:176px;">
      <p class="contact__name">Odile Varnet, M.A., CCC-SLP</p>
      <p>NJ Lic: 58KT00394817</p>
      <p>827 Quarry Ln. Lowmere, KV 07391</p>
      <p class="contact__row" style="margin-top:10px;"><span class="bullet bullet--green"></span>201-555-0148</p>
      <p class="contact__row"><span class="bullet bullet--orange"></span>Odile.Varnet@mailbrook.net</p>
      <p class="contact__row"><span class="bullet bullet--green"></span>www.ClearSoundHarbor.net</p>
    </div>
  </section>
  <p class="label label--front-1">Front-1</p>

  <section class="card card--front-2">
    <svg class="edge-band edge-band--right" viewBox="0 0 26 302" aria-hidden="true">
      <polygon points="0,0 26,0 26,200 0,170" fill="var(--green)"/>
      <polygon points="0,176 26,206 26,302 0,302" fill="var(--orange)"/>
    </svg>
    <div class="brand" style="left:34px; top:96px; font-size:20px;">
      <span class="brand__dot"></span>Clear Sound Harbor
    </div>
    <div class="contact" style="left:210px; top:196px; width:110px; text-align:right;">
      <p class="contact__name" style="color:var(--orange);">Odile Varnet,<br>M.A., CCC-SLP</p>
    </div>
    <div class="contact" style="left:336px; top:180px;">
      <p>NJ Lic: 58KT00394817</p>
      <p>827 Quarry Ln.</p>
      <p>Lowmere, KV 07391</p>
      <p class="contact__row" style="margin-top:8px;"><span class="bullet bullet--orange"></span>201-555-0148</p>
      <p class="contact__row"><span class="bullet bullet--orange"></span>Odile.Varnet@mailbrook.net</p>
      <p class="contact__row"><span class="bullet bullet--orange"></span>www.ClearSoundHarbor.net</p>
    </div>
  </section>
  <p class="label label--front-2">Front-2</p>

  <section class="card card--back-1">
    <svg class="edge-band edge-band--right" viewBox="0 0 26 302" aria-hidden="true">
      <polygon points="0,0 26,0 26,150 0,126" fill="var(--green)"/>
      <polygon points="0,132 26,156 26,302 0,302" fill="var(--orange)"/>
    </svg>
    <div class="brand" style="left:0; width:524px; justify-content:center; top:124px; font-size:34px;">
      <span class="brand__dot"></span>Clear Sound Harbor
    </div>
    <p class="website" style="width:524px; top:260px;">www.ClearSoundHarbor.net</p>
  </section>
  <p class="label label--back-1">Back-1</p>

  <section class="card card--back-2">
    <svg class="edge-band edge-band--left" viewBox="0 0 26 302" aria-hidden="true">
      <polygon points="0,0 26,0 26,130 0,160" fill="var(--orange)"/>
      <polygon points="0,166 26,136 26,302 0,302" fill="var(--green)"/>
    </svg>
    <div class="brand" style="left:26px; width:524px; justify-content:center; top:126px; font-size:26px;">
      <span class="brand__dot"></span>Clear Sound Harbor
    </div>
    <p class="website" style="left:26px; width:524px; top:260px;">www.ClearSoundHarbor.net</p>
  </section>
  <p class="label label--back-2">Back-2</p>

</body>
</html>
```